Business Card Colourful and fun Design Project

I need a business card design for my Ecommerce website which am launching soon. we are based in the United Arab Emirates and our customers are based in Dubai and other cities in UAE, In addition to our neighbour countries in the GCC. We sell Gadgets, fashion and other trendy stuff that are hard to find in our market. The company name is "ZIPKOALA" logo consists of a panda wearing traditional local Arab thobe. would like to see a clean, colourful fun design to represent us.
Updates
please read the discussion board. thanks
Industry/Entity Type
Fashion
Look and feel
Each slider illustrates characteristics of the customer's brand and the style your logo design should communicate.

```html
<!DOCTYPE html>
<html lang="en">
<head>
<meta charset="utf-8">
<title>ZIPKOALA business cards</title>
<link href="https://fonts.googleapis.com/css2?family=PT+Sans:wght@400;700&family=PT+Sans+Narrow:wght@400;700&display=swap" rel="stylesheet">
<style>
  :root{
    --brand-red:#b3121c;
    --ink:#1a1a1a;
    --card-edge:#d4d4d4;
    --paper:#ffffff;
    --art-light:#eef1f2;
    --art-mid:#c9cfd2;
    --art-accent:#d9a3a3;
  }
  *{margin:0;padding:0;box-sizing:border-box}
  html,body{width:1200px;height:1000px;overflow:hidden;background:var(--paper)}
  body{position:relative;font-family:"PT Sans",sans-serif;color:var(--brand-red)}
  .version-label{position:absolute;left:78px;font-family:"PT Sans",sans-serif;font-size:17px;color:var(--ink);letter-spacing:.3px}
  .card{position:absolute;width:498px;height:287px;border:1px solid var(--card-edge);background:var(--paper);overflow:hidden}
  .card > *{position:absolute;line-height:1;white-space:nowrap}
  .mascot-art{border-radius:10px;background:linear-gradient(160deg,var(--art-accent) 0%,var(--art-light) 30%,var(--art-mid) 100%)}
  .mascot-art.large{border-radius:60px 60px 0 0;background:linear-gradient(170deg,var(--art-accent) 0%,var(--art-light) 28%,var(--art-mid) 100%)}
  .wordmark{font-family:"PT Sans",sans-serif;font-weight:700;font-size:40px;letter-spacing:1.5px;color:var(--brand-red)}
  .tagline{font-family:"PT Sans",sans-serif;font-size:13px;letter-spacing:.2px}
  .tagline strong{font-weight:700;margin-left:6px}
  .hotline{display:flex;align-items:center;gap:9px;font-family:"PT Sans Narrow",sans-serif;font-weight:700;font-size:27px}
  .social{display:flex;align-items:center;gap:8px;font-family:"PT Sans Narrow",sans-serif;font-weight:700;font-size:14px}
  .social-mark{width:22px;height:22px;background:var(--brand-red);display:inline-block}
  .website{font-family:"PT Sans",sans-serif;font-weight:700;font-size:17px}
  .person-name{font-family:"PT Sans Narrow",sans-serif;font-size:27px}
  .person-title{font-family:"PT Sans Narrow",sans-serif;font-size:15px}
  .contact{display:flex;align-items:center;gap:10px;font-family:"PT Sans Narrow",sans-serif;font-size:17px}
  .centered{left:0;width:100%;text-align:center;justify-content:center}
  .right-aligned{right:39px;text-align:right;justify-content:flex-end}
</style>
</head>
<body>

<svg width="0" height="0" style="position:absolute">
  <defs>
    <symbol id="icon-phone" viewBox="0 0 46 28">
      <path d="M2 9 C2 2 44 2 44 9 L44 12 L34 12 L33 8 L13 8 L12 12 L2 12 Z" fill="currentColor"/>
      <path d="M13 11 L33 11 L40 26 L6 26 Z" fill="currentColor"/>
      <circle cx="23" cy="18.5" r="4.5" fill="#fff"/>
      <circle cx="23" cy="18.5" r="2" fill="currentColor"/>
    </symbol>
    <symbol id="icon-mail" viewBox="0 0 36 24">
      <rect x="1.5" y="1.5" width="33" height="21" fill="none" stroke="currentColor" stroke-width="2"/>
      <path d="M1.5 1.5 L18 14 L34.5 1.5" fill="none" stroke="currentColor" stroke-width="2"/>
    </symbol>
  </defs>
</svg>

<div class="version-label" style="top:117px">VERSION 1</div>
<div class="version-label" style="top:546px">VERSION 2</div>

<!-- Version 1, front -->
<section class="card" style="left:78px;top:152px">
  <div class="mascot-art" role="img" aria-label="Mascot illustration: a koala in a traditional white thobe and red checked headscarf" style="left:72px;top:18px;width:96px;height:116px"></div>
  <div class="wordmark" style="left:167px;top:61px">ZIPKOALA</div>
  <div class="tagline" style="left:175px;top:109px">YOU CAN’T FIND IT?<strong>WE’VE GOT IT!</strong></div>
  <div class="hotline centered" style="top:162px"><svg width="46" height="28"><use href="#icon-phone"/></svg>800 KOALA (56252)</div>
  <div class="social" style="left:62px;top:215px"><span class="social-mark"></span>zipkoalauae</div>
  <div class="social" style="left:194px;top:215px"><span class="social-mark"></span>@zipkoalauae</div>
  <div class="social" style="left:327px;top:215px"><span class="social-mark"></span>zipkoalauae</div>
  <div class="website centered" style="top:251px">www.zipkoala.com</div>
</section>

<!-- Version 1, personal -->
<section class="card" style="left:625px;top:152px">
  <div class="mascot-art" role="img" aria-label="Mascot illustration: a koala in a traditional white thobe and red checked headscarf" style="left:72px;top:18px;width:96px;height:116px"></div>
  <div class="wordmark" style="left:167px;top:61px">ZIPKOALA</div>
  <div class="tagline" style="left:175px;top:109px">YOU CAN’T FIND IT?<strong>WE’VE GOT IT!</strong></div>
  <div class="person-name centered" style="top:146px">SAM CARTER</div>
  <div class="person-title centered" style="top:178px">Senior Manager</div>
  <div class="contact" style="left:73px;top:218px"><svg width="34" height="22"><use href="#icon-phone"/></svg>1234 123 123</div>
  <div class="contact" style="left:218px;top:218px"><svg width="34" height="22"><use href="#icon-mail"/></svg>samcarter@zipkoala.com</div>
  <div class="website centered" style="top:251px">www.zipkoala.com</div>
</section>

<!-- Version 2, front -->
<section class="card" style="left:78px;top:580px">
  <div class="mascot-art large" role="img" aria-label="Large mascot illustration: a koala in a white thobe and red checked headscarf resting its chin on its paws" style="left:17px;top:25px;width:182px;height:262px"></div>
  <div class="wordmark" style="left:214px;top:33px">ZIPKOALA</div>
  <div class="tagline" style="left:214px;top:82px">YOU CAN’T FIND IT?<strong>WE’VE GOT IT!</strong></div>
  <div class="hotline" style="left:224px;top:122px"><svg width="38" height="24"><use href="#icon-phone"/></svg><span style="font-size:24px">800 KOALA (56252)</span></div>
  <div class="social" style="left:217px;top:176px"><span class="social-mark"></span>zipkoalauae</div>
  <div class="social" style="left:344px;top:176px"><span class="social-mark"></span>@zipkoalauae</div>
  <div class="social" style="left:280px;top:206px"><span class="social-mark"></span>zipkoalauae</div>
  <div class="website" style="left:214px;width:248px;text-align:center;top:244px">www.zipkoala.com</div>
</section>

<!-- Version 2, personal -->
<section class="card" style="left:625px;top:580px">
  <div class="mascot-art large" role="img" aria-label="Large mascot illustration: a koala in a white thobe and red checked headscarf resting its chin on its paws" style="left:17px;top:25px;width:182px;height:262px"></div>
  <div class="wordmark" style="left:217px;top:36px">ZIPKOALA</div>
  <div class="tagline" style="left:214px;top:85px">YOU CAN’T FIND IT?<strong>WE’VE GOT IT!</strong></div>
  <div class="person-name right-aligned" style="top:119px">SAM CARTER</div>
  <div class="person-title right-aligned" style="top:152px">Senior Manager</div>
  <div class="contact right-aligned" style="top:192px"><svg width="30" height="20"><use href="#icon-phone"/></svg>1234 123 123</div>
  <div class="contact right-aligned" style="top:219px"><svg width="28" height="19"><use href="#icon-mail"/></svg>samcarter@zipkoala.com</div>
  <div class="website right-aligned" style="top:249px">www.zipkoala.com</div>
</section>

</body>
</html>
```